Cardiology practice business card

We need a business card for our cardiology practice "Bellmoor Cardiology". We have a new logo, attached below. We like the colours in the logo - red and charcoal. The front of the business card will need to have the doctors name, address, phone number and email. The back will need to have space to write 2 appointment dates and times.

```html
<!DOCTYPE html>
<html lang="en">
<head>
<meta charset="utf-8">
<title>Bellmoor Cardiology – Business Card</title>
<link href="https://fonts.googleapis.com/css2?family=Montserrat:wght@400;500;700&display=swap" rel="stylesheet">
<style>
  :root {
    --red: #e0312f;
    --charcoal: #4a4a4d;
    --ink: #2a2a2a;
    --rule: #8a8a8a;
    --paper: #ffffff;
    --backdrop: #3c3c3e;
  }
  * { box-sizing: border-box; margin: 0; padding: 0; }
  html, body { width: 1200px; height: 875px; overflow: hidden; }
  body {
    background: var(--backdrop);
    font-family: "Montserrat", sans-serif;
    display: flex;
    align-items: center;
    justify-content: center;
    gap: 60px;
  }
  .card {
    position: relative;
    width: 525px;
    height: 300px;
    background: var(--paper);
    border-radius: 18px;
    overflow: hidden;
    box-shadow: 0 20px 40px rgba(0,0,0,0.45);
  }
  .card::after {
    content: "";
    position: absolute;
    left: 0; right: 0; bottom: 0;
    height: 8px;
    background: var(--red);
  }
  .brand {
    position: absolute;
    top: 34px;
    right: 34px;
    display: flex;
    align-items: center;
    gap: 10px;
    color: var(--charcoal);
    font-weight: 700;
    font-size: 22px;
    letter-spacing: 0.04em;
    text-transform: uppercase;
  }
  .brand-dot {
    width: 14px; height: 14px;
    border-radius: 50%;
    background: var(--red);
  }

  /* Back: appointment card */
  .write-line {
    position: absolute;
    height: 1px;
    background: var(--rule);
  }
  .write-line.top1 { left: 250px; right: 34px; top: 110px; }
  .write-line.top2 { left: 150px; right: 34px; top: 150px; }
  .appointment-title {
    position: absolute;
    left: 36px;
    top: 180px;
    color: var(--red);
    font-weight: 700;
    font-size: 20px;
  }
  .field {
    position: absolute;
    left: 36px;
    right: 34px;
    display: flex;
    align-items: flex-end;
    gap: 6px;
    font-size: 12px;
    font-weight: 500;
    color: var(--ink);
  }
  .field .fill { flex: 1; height: 1px; background: var(--rule); margin-bottom: 3px; }
  .field.time { top: 222px; }
  .field.date { top: 256px; }

  /* Front: contact card */
  .person { position: absolute; left: 36px; top: 118px; }
  .person-name { color: var(--red); font-weight: 700; font-size: 20px; }
  .person-role { color: var(--ink); font-size: 12px; margin-top: 2px; }
  .address {
    position: absolute;
    left: 36px; top: 184px;
    font-size: 12px; line-height: 1.35;
    color: var(--ink);
  }
  .contacts {
    position: absolute;
    left: 36px; top: 224px;
    list-style: none;
    font-size: 12px;
    color: var(--ink);
  }
  .contacts li { display: flex; align-items: center; gap: 8px; line-height: 1.45; }
  .contacts svg { width: 11px; height: 11px; fill: var(--red); flex: none; }
</style>
</head>
<body>

  <section class="card card-back" aria-label="Appointment side">
    <div class="brand"><span class="brand-dot"></span>Bellmoor Cardiology</div>
    <div class="write-line top1"></div>
    <div class="write-line top2"></div>
    <h2 class="appointment-title">Next Apointment</h2>
    <div class="field time"><span>Time:</span><span class="fill"></span></div>
    <div class="field date"><span>Date:</span><span class="fill"></span></div>
  </section>

  <section class="card card-front" aria-label="Contact side">
    <div class="brand"><span class="brand-dot"></span>Bellmoor Cardiology</div>
    <div class="person">
      <h1 class="person-name">Daniel Hart</h1>
      <p class="person-role">Managing Director</p>
    </div>
    <address class="address" style="font-style:normal">
      415 Linden Park Ave, #112<br>
      Ashford, OH 43210
    </address>
    <ul class="contacts">
      <li>
        <svg viewBox="0 0 24 24"><path d="M6.6 10.8a15 15 0 0 0 6.6 6.6l2.2-2.2a1 1 0 0 1 1-.25 11.4 11.4 0 0 0 3.6.57 1 1 0 0 1 1 1V20a1 1 0 0 1-1 1A17 17 0 0 1 3 4a1 1 0 0 1 1-1h3.5a1 1 0 0 1 1 1c0 1.25.2 2.45.57 3.57a1 1 0 0 1-.25 1z"/></svg>
        555-214-0187
      </li>
      <li>
        <svg viewBox="0 0 24 24"><path d="M2 5h20v14H2z M2 5l10 8 10-8" stroke="#fff" stroke-width="1.5"/></svg>
        info@bellmoorcardiology.com
      </li>
      <li>
        <svg viewBox="0 0 24 24"><circle cx="12" cy="12" r="10"/><path d="M2 12h20M12 2c3 3 3 17 0 20M12 2c-3 3-3 17 0 20" stroke="#fff" stroke-width="1.5" fill="none"/></svg>
        www.bellmoorcardiology.com
      </li>
    </ul>
  </section>

</body>
</html>
```